Heronbrook Custom Woodcraft Website design

Need a small website to showcase my products and take orders

would also like payment options

We do custom wood work along with cnc work in wood plastic and soft metals

we are based in edmonton alberta canada
Updates

Industry/Entity Type

Work

Number of Pages Required

3 page

Requirements
Nice to have
• Interview for for a woodworking magazine
• http://grainandplaneweekly.example/issue-1-02-august-2016/member-spotlight
• I would also like to see metal working/branding iron info
• Also adding the picture of me from the above interview is a nice touch

```html
<!DOCTYPE html>
<html lang="en">
<head>
<meta charset="utf-8">
<title>Heronbrook Custom Woodcraft</title>
<link rel="stylesheet" href="https://fonts.googleapis.com/css2?family=Oswald:wght@400;500&family=Roboto:wght@300;400;500&display=swap">
<style>
:root{
  --accent:#c0825a;
  --nav:#c68b63;
  --ink:#2b2b2b;
  --body:#7a7a7a;
  --light:#f2f2f2;
  --footer:#6f5045;
  --footer-dark:#6a4b40;
  --white:#ffffff;
}
*{box-sizing:border-box;margin:0;padding:0}
html,body{width:1200px;height:2419px;overflow:hidden;background:var(--white);font-family:"Roboto",sans-serif;color:var(--ink)}
.page{position:relative;width:1200px;height:2419px}
.abs{position:absolute}

/* header */
.phone{left:89px;top:40px;display:flex;align-items:center;gap:14px;font-size:20px;color:#333}
.phone-ring{width:40px;height:40px;border:2px solid #444;border-radius:50%;display:flex;align-items:center;justify-content:center}
.brand{left:0;width:1200px;top:26px;text-align:center}
.brand-name{display:inline-flex;align-items:center;gap:14px;font-family:"Oswald",sans-serif;font-size:34px;font-weight:500;color:#6a4a3c;letter-spacing:1px;text-transform:uppercase}
.brand-dot{width:22px;height:22px;border-radius:50%;background:#6a4a3c}
.social-top{left:1003px;top:45px;display:flex;gap:10px}
.social-top span{width:18px;height:18px;border-radius:3px;background:#666}

/* hero */
.hero{left:0;top:110px;width:1200px;height:561px;background:linear-gradient(180deg,#5d4636 0%,#8a6a4e 45%,#a47e58 70%,#d8d2cc 100%)}
.nav{left:89px;top:110px;width:1022px;height:62px}
.nav-links{left:89px;top:120px;width:1022px;display:flex;justify-content:space-around;padding:0 50px;font-size:14.5px;color:var(--white);text-transform:uppercase;letter-spacing:.3px}
.hero-title{left:0;width:1200px;top:362px;text-align:center;font-family:"Oswald",sans-serif;font-size:58px;font-weight:500;color:var(--white);text-shadow:0 2px 6px rgba(0,0,0,.4)}
.hero-sub{left:0;width:1200px;top:438px;text-align:center;font-family:"Oswald",sans-serif;font-size:28px;line-height:37px;color:var(--white);text-shadow:0 2px 6px rgba(0,0,0,.4)}
.hero-arrow{top:409px;width:35px;height:35px;background:#1e1e1e;display:flex;align-items:center;justify-content:center}

/* sections */
.heading{left:0;width:1200px;text-align:center;font-size:26px;font-weight:400;text-transform:uppercase;color:var(--ink)}
.heading em{font-style:normal;color:var(--accent)}
.welcome-text{left:113px;width:974px;top:767px;text-align:center;font-size:13.8px;line-height:24px;color:var(--body)}
.band{left:0;width:1200px;background:var(--light)}

.craft-card{top:969px;width:246px;height:318px;background:linear-gradient(180deg,#fff 0%,#f0f0f0 100%);border:1px solid #dcdcdc;box-shadow:0 1px 3px rgba(0,0,0,.08)}
.craft-img{width:100%;height:183px}
.craft-title{margin-top:32px;text-align:center;font-size:16px;color:#333;text-transform:uppercase}
.craft-text{margin:10px auto 0;width:200px;text-align:center;font-size:14.5px;line-height:24px;color:var(--body)}

.article{top:1411px;width:316px}
.article-img{position:relative;width:316px;height:194px;border:4px solid #fff;box-shadow:0 0 0 1px #ddd}
.date{position:absolute;left:0;top:48px;width:50px;color:#fff;text-align:center}
.date-day{background:#8a6a55;height:56px;padding-top:5px;font-size:20px;line-height:24px}
.date-day small{display:block;font-size:11px;text-transform:uppercase}
.date-year{background:#222;height:36px;line-height:36px;font-size:15px}
.article-title{margin-top:16px;font-size:15px;color:#333}
.article-text{margin-top:14px;font-size:12px;line-height:20px;color:var(--body);height:40px;overflow:hidden}
.more{margin-top:6px;font-size:12px;color:#7a4a35}

.product{top:1839px;width:248px;height:266px}
.product-overlay{position:absolute;inset:0;background:rgba(0,0,0,.55);display:flex;flex-direction:column;align-items:center;justify-content:center}
.product-actions{display:flex;gap:10px;margin-top:40px}
.product-actions span{width:44px;height:44px;border-radius:50%;background:var(--accent);display:flex;align-items:center;justify-content:center}
.product-label{margin-top:20px;color:#fff;font-size:17px;text-transform:uppercase}

/* footer */
.footer{left:0;top:2150px;width:1200px;height:210px;background:var(--footer)}
.footbar{left:0;top:2360px;width:1200px;height:59px;background:var(--footer-dark);border-top:1px solid #8a6e63;text-align:center;line-height:58px;color:#fff;font-size:14px}
.col{top:2185px;color:#fff}
.col h4{font-size:15.5px;font-weight:400;text-transform:uppercase;margin-bottom:16px}
.col p{font-size:12.5px;line-height:20px}
.contact-row{display:flex;align-items:center;gap:14px;font-size:16px;margin-top:8px}
.contact-row.small{font-size:13.5px}
.news-form{display:flex;margin-top:18px}
.news-input{width:168px;height:38px;background:#fff;font-size:11px;color:#888;padding:12px 12px}
.news-btn{width:82px;height:38px;background:#3a2e2a;color:#fff;font-size:16px;text-align:center;line-height:38px}
.social-foot{display:flex;gap:18px;margin-top:14px}
.social-foot span{width:34px;height:34px;background:#f2f2f2;border-radius:4px}
</style>
</head>
<body>
<div class="page">

  <!-- header -->
  <div class="abs phone">
    <span class="phone-ring">
      <svg width="18" height="18" viewBox="0 0 24 24"><path d="M6.6 10.8a15 15 0 0 0 6.6 6.6l2.2-2.2a1 1 0 0 1 1-.25 11.4 11.4 0 0 0 3.6.57 1 1 0 0 1 1 1V20a1 1 0 0 1-1 1A17 17 0 0 1 3 4a1 1 0 0 1 1-1h3.5a1 1 0 0 1 1 1c0 1.25.2 2.45.57 3.57a1 1 0 0 1-.25 1z" fill="none" stroke="#444" stroke-width="1.6"/></svg>
    </span>
    0455 218 904
  </div>
  <div class="abs brand"><span class="brand-name"><span class="brand-dot"></span>Heronbrook Custom Woodcraft</span></div>
  <div class="abs social-top"><span></span><span></span><span></span><span></span></div>

  <!-- hero -->
  <div class="abs hero" role="img" aria-label="Photograph of three cedar folding stools with engraved seat panels against a wooden wall"></div>
  <svg class="abs nav" viewBox="0 0 1022 62" width="1022" height="62"><path d="M0 0H1022V44Q511 66 0 44Z" fill="var(--nav)"/></svg>
  <nav class="abs nav-links"><span>Home</span><span>Services</span><span>Production</span><span>Portfolio</span><span>About Us</span><span>Articles</span><span>Contact Us</span></nav>
  <div class="abs hero-title">HERONBROOK WOODCRAFT</div>
  <div class="abs hero-sub">We do custom wood work along with cnc work<br>in wood plastic and soft metals</div>
  <div class="abs hero-arrow" style="left:61px"><svg width="12" height="18" viewBox="0 0 12 18"><path d="M9 2 3 9l6 7" fill="none" stroke="#fff" stroke-width="1.6"/></svg></div>
  <div class="abs hero-arrow" style="left:1110px"><svg width="12" height="18" viewBox="0 0 12 18"><path d="M3 2l6 7-6 7" fill="none" stroke="#fff" stroke-width="1.6"/></svg></div>

  <!-- welcome -->
  <h2 class="abs heading" style="top:722px">Welcome to <em>Heronbrook Wood Craft</em></h2>
  <p class="abs welcome-text">Lorem Ipsum has been the industry's standard dummy text ever since the 1500s, when an unknown printer took a galley of type and scrambled it to make a type specimen book. It has survived not only five centuries, but also the leap into electronic typesetting, remaining essentially unchanged. It was popularised in the 1960s with the release of Transferline sheets containing Lorem Ipsum passages, and more recently with desktop publishing software like Folio PageSetter</p>

  <!-- custom wood craft -->
  <div class="abs band" style="top:876px;height:451px"></div>
  <h2 class="abs heading" style="top:910px">Custom <em>Wood Craft</em></h2>
  <div class="abs craft-card" style="left:93px"><div class="craft-img" role="img" aria-label="Carved oval cribbage board in light wood" style="background:radial-gradient(ellipse at center,#c9a27a 0%,#9c7552 55%,#2a2420 100%)"></div><div class="craft-title">Products</div><p class="craft-text">Neque porro quisquam est qui dolorem ipsum</p></div>
  <div class="abs craft-card" style="left:351px"><div class="craft-img" role="img" aria-label="Carved bird relief in reddish wood" style="background:radial-gradient(ellipse at center,#a35a3a 0%,#7e3c26 60%,#5a2a1a 100%)"></div><div class="craft-title">Products</div><p class="craft-text">Neque porro quisquam est qui dolorem ipsum</p></div>
  <div class="abs craft-card" style="left:608px"><div class="craft-img" role="img" aria-label="Round engraved plaque of a building in dark wood" style="background:radial-gradient(circle at center,#6e5040 0%,#4a3428 55%,#8e8070 100%)"></div><div class="craft-title">Products</div><p class="craft-text">Neque porro quisquam est qui dolorem ipsum</p></div>
  <div class="abs craft-card" style="left:865px"><div class="craft-img" role="img" aria-label="Metal relief plate of a storefront scene" style="background:radial-gradient(ellipse at center,#b8b2a8 0%,#8a847a 55%,#1d1d1d 100%)"></div><div class="craft-title">Products</div><p class="craft-text">Neque porro quisquam est qui dolorem ipsum</p></div>

  <!-- interview -->
  <h2 class="abs heading" style="top:1355px">Our <em>Interview Article</em></h2>
  <article class="abs article" style="left:89px">
    <div class="article-img" role="img" aria-label="Three cedar stools in a workshop" style="background:linear-gradient(180deg,#8b6a4e,#c9a27a)">
      <div class="date"><div class="date-day">02<small>Jun</small></div><div class="date-year">2016</div></div>
    </div>
    <h3 class="article-title" style="font-weight:400">What is your "inspiration story"</h3>
    <p class="article-text">I grew up in a small logging community in British Columbia Canada. Wood and woodworking were always around. Some</p>
    <div class="more">Read More »</div>
  </article>
  <article class="abs article" style="left:442px">
    <div class="article-img" role="img" aria-label="Black engraved round sign on a CNC bed" style="background:radial-gradient(circle at 60% 50%,#3a3a3a,#121212 60%,#8a8a8a 100%)">
      <div class="date"><div class="date-day">02<small>Jun</small></div><div class="date-year">2016</div></div>
    </div>
    <h3 class="article-title" style="font-weight:400">Who is your woodworking mentor and why?</h3>
    <p class="article-text">My mentor would have to be my father. I have fond memories of him standing at the wood lathe with chips a</p>
    <div class="more">Read More »</div>
  </article>
  <article class="abs article" style="left:795px">
    <div class="article-img" role="img" aria-label="Turned wooden tool handle with shavings on a bench" style="background:linear-gradient(160deg,#c7955e,#a0622f 60%,#6d3f20)">
      <div class="date"><div class="date-day">02<small>Jun</small></div><div class="date-year">2016</div></div>
    </div>
    <h3 class="article-title" style="font-weight:400">Hand or power tools?</h3>
    <p class="article-text">I use mostly power tools, as it is quicker. I think it comes from my lack of patience. That is not to say I don't love the feel</p>
    <div class="more">Read More »</div>
  </article>

  <!-- products -->
  <div class="abs band" style="top:1744px;height:406px"></div>
  <h2 class="abs heading" style="top:1778px">Our <em>Products</em></h2>
  <div class="abs product" style="left:90px" role="img" aria-label="Black engraved round sign">
    <div style="position:absolute;inset:0;background:radial-gradient(circle,#3a3a3a,#111)"></div>
    <div class="product-overlay">
      <div class="product-actions">
        <span><svg width="18" height="18" viewBox="0 0 20 20"><circle cx="8" cy="8" r="6" fill="none" stroke="#fff" stroke-width="2"/><path d="M12.5 12.5 18 18M8 5v6M5 8h6" stroke="#fff" stroke-width="2"/></svg></span>
        <span><svg width="18" height="16" viewBox="0 0 20 18"><path d="M10 17 2.5 9.5A4.5 4.5 0 0 1 10 3.5a4.5 4.5 0 0 1 7.5 6z" fill="#fff"/></svg></span>
      </div>
      <div class="product-label">Wood Craft</div>
    </div>
  </div>
  <div class="abs product" style="left:348px" role="img" aria-label="Dark oval carved cribbage board" style="background:#555"><div style="position:absolute;inset:0;background:radial-gradient(ellipse,#6a5a4e,#3d342e 60%,#8a8a86)"></div></div>
  <div class="abs product" style="left:606px" role="img" aria-label="Wooden wall cabinet with two doors"><div style="position:absolute;inset:0;background:linear-gradient(180deg,#a88b6c,#6e5238 50%,#a88b6c)"></div></div>
  <div class="abs product" style="left:864px" role="img" aria-label="Carved log sculpture on a stone counter"><div style="position:absolute;inset:0;background:linear-gradient(180deg,#b9b3a8,#4a3a2c 40%,#2e241c 80%,#6b5a4a)"></div></div>
  <svg class="abs" style="left:42px;top:1940px" width="22" height="44" viewBox="0 0 22 44"><path d="M20 2 2 22l18 20" fill="none" stroke="#222" stroke-width="2"/></svg>
  <svg class="abs" style="left:1138px;top:1940px" width="22" height="44" viewBox="0 0 22 44"><path d="M2 2l18 20L2 42" fill="none" stroke="#222" stroke-width="2"/></svg>

  <!-- footer -->
  <footer class="abs footer"></footer>
  <div class="abs col" style="left:90px">
    <h4>Contact Us</h4>
    <p>42 Millrace Lane, Suite 3<br>Edmonton, AB T5K 0L2, Canada</p>
    <div class="contact-row" style="margin-top:14px"><svg width="18" height="18" viewBox="0 0 24 24"><path d="M6.6 10.8a15 15 0 0 0 6.6 6.6l2.2-2.2a1 1 0 0 1 1-.25 11.4 11.4 0 0 0 3.6.57 1 1 0 0 1 1 1V20a1 1 0 0 1-1 1A17 17 0 0 1 3 4a1 1 0 0 1 1-1h3.5a1 1 0 0 1 1 1c0 1.25.2 2.45.57 3.57a1 1 0 0 1-.25 1z" fill="none" stroke="#fff" stroke-width="1.5"/></svg>(+780) 555-0142</div>
    <div class="contact-row small"><svg width="18" height="14" viewBox="0 0 20 14"><rect x="1" y="1" width="18" height="12" fill="none" stroke="#fff" stroke-width="1.4"/><path d="M1 1l9 7 9-7" fill="none" stroke="#fff" stroke-width="1.4"/></svg>hello@heronbrook.example</div>
  </div>
  <div class="abs col" style="left:364px;width:230px">
    <h4>Latest Tweet's</h4>
    <div style="display:flex;gap:14px">
      <span style="flex:none;width:16px;height:16px;background:#f2f2f2;border-radius:2px;margin-top:2px"></span>
      <p style="font-size:11.5px;line-height:19px">Phasellus porta. Fusce susct varius mi. Cum sociis natoque penabus et magnis dis parturient montes, nascetur ridiculus mus. See more here http://short.example/hb7Kq2</p>
    </div>
  </div>
  <div class="abs col" style="left:672px;width:250px">
    <h4>Newsletter</h4>
    <p style="font-size:11.5px;line-height:19px">Excepteur sint occaecat cupidatat non proident, sunt in culpa qui officia deserunt mollit anim</p>
    <div class="news-form"><div class="news-input">Enter your email address</div><div class="news-btn">Sign Up</div></div>
  </div>
  <div class="abs col" style="left:978px">
    <h4>Social Media</h4>
    <div class="social-foot"><span></span><span></span><span></span></div>
  </div>
  <div class="abs footbar">2016 &nbsp;All Rights Reserved.</div>

</div>
</body>
</html>
```